Employee Benefits Flyer for Recruiting

We are a Steel Product Supplier and Manufacturer in Toledo Ohio.

We would like to create an "attention getting", one-page handout to give prospective employees (both production and administrative) that illustrates all the benefits we offer as a company. An editable document would be preferable as we add more or change existing benefits in the future. Current benefits include:

Individual and Family Medical Insurance
Dental Insurance
Vision Insurance
Short Term Disability Insurance
Critical Illness and Accident Insurance
No Cost Life Insurance Policy
Education Cost Reimbursement
401K with Company Match
Profit Sharing
Attendance and Performance Bonuses
No Cost Legal Assistance
No Cost Counseling Services
No Cost Tobacco Cessation Coaching
No Cost College Planning Assistance
No Cost Work-Life Services
No Cost Employee Discounts
No Cost Legal Consultation
No Cost Financial Consultation
No Cost ID Theft Assistance
No Cost Tax Consultation Assistance
Up to 17 Days of Paid Time Off

Target Market(s)

Potential Employees

Industry/Entity Type

Industrial Manufacturing

Requirements
Must have
• Nicely laid out illustrations / engaging content

```html
<!DOCTYPE html>
<html lang="en">
<head>
<meta charset="utf-8">
<title>Why Tollmere? – Employee Benefits</title>
<link href="https://fonts.googleapis.com/css2?family=Archivo+Black&family=Rubik:wght@500;800&display=swap" rel="stylesheet">
<style>
  :root {
    --navy-deep: #0a1224;
    --steel-blue: #1e4f96;
    --brand-blue: #0b5ad8;
    --brand-blue-dark: #0a3f9e;
    --white: #ffffff;
    --frame: rgba(200, 210, 225, 0.55);
    --panel: rgba(6, 12, 26, 0.55);
  }
  * { box-sizing: border-box; margin: 0; padding: 0; }
  html, body { width: 990px; height: 1200px; overflow: hidden; background: var(--navy-deep); }
  .flyer {
    position: relative; width: 990px; height: 1200px; overflow: hidden;
    font-family: "Rubik", Arial, sans-serif; color: var(--white);
  }
  .site-photo {
    position: absolute; inset: 0;
    background:
      linear-gradient(180deg, rgba(20,24,32,0.95) 0%, rgba(16,38,78,0.85) 22%, rgba(14,40,86,0.8) 55%, rgba(8,18,34,0.95) 85%, #05080f 100%),
      linear-gradient(90deg, #18243a 0%, #1c3f7a 50%, #142a52 100%);
  }
  .brand-mark {
    position: absolute; left: 168px; top: 48px; width: 114px; height: 114px;
    border-radius: 50%; background: var(--brand-blue);
  }
  .brand-name {
    position: absolute; left: 58px; top: 212px; width: 336px; text-align: center;
    font-weight: 800; font-size: 25px; letter-spacing: 0.5px; line-height: 1.05;
  }
  .brand-name small {
    display: flex; align-items: center; justify-content: center; gap: 10px;
    font-size: 11px; font-weight: 500; letter-spacing: 7px; margin-top: 5px;
  }
  .brand-name small::before, .brand-name small::after {
    content: ""; width: 74px; height: 1.5px; background: var(--white);
  }
  .website {
    position: absolute; right: 54px; top: 58px;
    font-weight: 800; font-size: 15px; letter-spacing: 3.2px;
  }
  .title-band {
    position: absolute; left: 366px; top: 88px; width: 624px; height: 79px;
    background: linear-gradient(90deg, var(--brand-blue-dark), var(--brand-blue));
    clip-path: polygon(0 0, 100% 0, 100% 100%, 6% 100%);
  }
  .title {
    position: absolute; right: 54px; top: 97px;
    font-family: "Archivo Black", "Arial Black", sans-serif; font-size: 50px; line-height: 60px; letter-spacing: 0.5px;
  }
  .benefits { position: absolute; width: 404px; list-style: none; }
  .benefits--left { left: 58px; top: 292px; }
  .benefits--right { left: 528px; top: 204px; }
  .benefit {
    position: relative; height: 83px; margin-bottom: 4.6px;
    border: 1.5px solid var(--frame); background: var(--panel);
    display: flex; align-items: center;
  }
  .benefit-icon {
    position: absolute; left: 4px; top: 4px; bottom: 4px; width: 70px;
    background: linear-gradient(135deg, var(--brand-blue), var(--steel-blue));
    display: flex; align-items: center; justify-content: center;
  }
  .benefit-icon svg { width: 40px; height: 40px; fill: none; stroke: var(--white); stroke-width: 1.6; stroke-linecap: round; stroke-linejoin: round; }
  .benefit-text { margin-left: 92px; font-size: 21.5px; line-height: 26px; font-weight: 500; white-space: nowrap; }
  .benefit-text strong { display: block; font-weight: 800; letter-spacing: 0.3px; }
</style>
</head>
<body>
<main class="flyer">
  <div class="site-photo" role="img" aria-label="Dusk aerial photo of the company's blue steel warehouse building"></div>

  <div class="brand-mark"></div>
  <div class="brand-name">TOLLMERE STEEL<small>SERVICES</small></div>

  <div class="website">www.tollmere-steel.example</div>
  <div class="title-band"></div>
  <h1 class="title">WHY TOLLMERE?</h1>

  <ul class="benefits benefits--left">
    <li class="benefit"><span class="benefit-icon"><svg viewBox="0 0 32 32"><path d="M16 14c-3-3-7-1-6 2 1 2 6 6 6 6s5-4 6-6c1-3-3-5-6-2z"/><path d="M15 8h2M16 7v2"/><path d="M4 14v8l6 5v3M28 14v8l-6 5v3"/></svg></span><p class="benefit-text"><strong>Individual and</strong>Family Medical Insurance</p></li>
    <li class="benefit"><span class="benefit-icon"><svg viewBox="0 0 32 32"><path d="M9 6c3-1 5 1 7 1s4-2 7-1c3 1 3 6 2 9s-1 10-3 11-2-7-6-7-4 8-6 7-2-8-3-11-1-8 2-9z"/><path d="M22 18l3 1v3l-3 2-3-2v-3z"/></svg></span><p class="benefit-text"><strong>Dental</strong>Insurance</p></li>
    <li class="benefit"><span class="benefit-icon"><svg viewBox="0 0 32 32"><path d="M16 3l11 4v8c0 7-5 12-11 14C10 27 5 22 5 15V7z"/><path d="M9 16s3-4 7-4 7 4 7 4-3 4-7 4-7-4-7-4z"/><circle cx="16" cy="16" r="2"/></svg></span><p class="benefit-text"><strong>Vision</strong>Insurance</p></li>
    <li class="benefit"><span class="benefit-icon"><svg viewBox="0 0 32 32"><path d="M14 4l9 3v7c0 6-4 10-9 12-5-2-9-6-9-12V7z"/><circle cx="24" cy="9" r="4"/><path d="M24 7v4M22 9h4"/><circle cx="12" cy="19" r="3"/><path d="M12 11v5h4"/></svg></span><p class="benefit-text"><strong>Short Term</strong>Disability Insurance</p></li>
    <li class="benefit"><span class="benefit-icon"><svg viewBox="0 0 32 32"><circle cx="11" cy="8" r="3.5"/><path d="M4 24c0-6 3-10 7-10s5 2 6 4"/><path d="M22 15l6 2v4c0 4-3 6-6 7-3-1-6-3-6-7v-4z"/><path d="M19 21l2 2 4-4"/></svg></span><p class="benefit-text"><strong>Critical Illness and</strong>Accident Insurance</p></li>
    <li class="benefit"><span class="benefit-icon"><svg viewBox="0 0 32 32"><path d="M16 16c-3-3-8-1-7 3 1 3 7 6 7 6s6-3 7-6c1-4-4-6-7-3z"/><path d="M10 19h3l2-3 2 4 2-2h3"/><circle cx="24" cy="7" r="3"/><path d="M3 22h4l6 5h9l6-4"/></svg></span><p class="benefit-text"><strong>No Cost</strong>Life Insurance Policy</p></li>
    <li class="benefit"><span class="benefit-icon"><svg viewBox="0 0 32 32"><path d="M4 10l12-5 12 5-12 5z"/><path d="M9 12v5c3 2 11 2 14 0v-5"/><path d="M4 21h24v6H4z"/><path d="M16 21v6"/></svg></span><p class="benefit-text"><strong>Education Cost</strong>Reimbursement</p></li>
    <li class="benefit"><span class="benefit-icon"><svg viewBox="0 0 32 32"><path d="M4 4h10v4a2 2 0 010 4v2H4z"/><path d="M16 16h12v12H16z"/><path d="M4 16h10v12H4z"/><path d="M18 6h8v8h-8z"/></svg></span><p class="benefit-text"><strong>401K with</strong>Company Match</p></li>
    <li class="benefit"><span class="benefit-icon"><svg viewBox="0 0 32 32"><circle cx="16" cy="16" r="12"/><path d="M16 4v12h12"/><path d="M11 14c-2 0-2 3 0 3s2 3 0 3M11 12v10M21 6c-2 0-2 3 0 3"/></svg></span><p class="benefit-text"><strong>Profit</strong>Sharing</p></li>
    <li class="benefit"><span class="benefit-icon"><svg viewBox="0 0 32 32"><path d="M3 5h26v13H3z"/><circle cx="9" cy="11" r="3"/><path d="M18 15v-3M22 15v-5M26 15V8"/><path d="M16 22v7M11 23l5 4 5-4"/></svg></span><p class="benefit-text"><strong>Attendance and</strong>Performance Bonuses</p></li>
  </ul>

  <ul class="benefits benefits--right">
    <li class="benefit"><span class="benefit-icon"><svg viewBox="0 0 32 32"><path d="M20 4H6v24h12"/><path d="M20 4l4 4v6"/><path d="M9 10h8M9 14h8M9 18h5"/><path d="M20 18l6 6M18 21l5-5 2 2-5 5z"/></svg></span><p class="benefit-text"><strong>No Cost</strong>Legal Assistance</p></li>
    <li class="benefit"><span class="benefit-icon"><svg viewBox="0 0 32 32"><circle cx="10" cy="8" r="3"/><path d="M4 20c0-5 3-8 6-8s6 3 6 6"/><circle cx="21" cy="17" r="3"/><path d="M15 28c0-4 3-7 6-7s6 3 6 7"/><path d="M19 4h9v6h-5l-2 2v-2h-2z"/></svg></span><p class="benefit-text"><strong>No Cost</strong>Counseling Services</p></li>
    <li class="benefit"><span class="benefit-icon"><svg viewBox="0 0 32 32"><circle cx="16" cy="16" r="13"/><path d="M7 25L25 7"/><path d="M7 17h16v4H7z"/><path d="M21 10c2 0 3 2 3 4"/></svg></span><p class="benefit-text"><strong>No Cost</strong>Tobacco Cessation Coaching</p></li>
    <li class="benefit"><span class="benefit-icon"><svg viewBox="0 0 32 32"><path d="M6 28V6h20v22"/><path d="M3 28h26"/><path d="M10 10h3M15 10h2M19 10h3M10 15h3M15 15h2M19 15h3"/><path d="M13 28v-6h6v6"/></svg></span><p class="benefit-text"><strong>No Cost</strong>College Planning Assistance</p></li>
    <li class="benefit"><span class="benefit-icon"><svg viewBox="0 0 32 32"><path d="M4 10h24v16H4z"/><path d="M12 10V7h8v3"/><path d="M4 17h24"/><path d="M15 15h2v4h-2z"/></svg></span><p class="benefit-text"><strong>No Cost</strong>Work-Life Services</p></li>
    <li class="benefit"><span class="benefit-icon"><svg viewBox="0 0 32 32"><path d="M16 3l3 3h4v4l3 3-3 3v4h-4l-3 3-3-3H9v-4l-3-3 3-3V6h4z" transform="translate(0 3)"/><path d="M12 21l8-8"/><circle cx="12.5" cy="14.5" r="1.5"/><circle cx="19.5" cy="19.5" r="1.5"/></svg></span><p class="benefit-text"><strong>No Cost</strong>Employee Discounts</p></li>
    <li class="benefit"><span class="benefit-icon"><svg viewBox="0 0 32 32"><path d="M8 4h20v14h-6"/><path d="M18 8v8M13 8h10M14 8l-2 5h4zM22 8l-2 5h4z"/><path d="M3 16h16v10H9l-4 3v-3H3z"/><path d="M6 20h10M6 23h7"/></svg></span><p class="benefit-text"><strong>No Cost</strong>Legal Consultation</p></li>
    <li class="benefit"><span class="benefit-icon"><svg viewBox="0 0 32 32"><path d="M9 5h18v14H9z"/><path d="M18 8v8M20 9c-3-1-4 2-2 3s1 4-2 3"/><path d="M3 17h8v7H5l-2 2z"/><path d="M20 21h8M20 24h8M20 27h8"/></svg></span><p class="benefit-text"><strong>No Cost</strong>Financial Consultation</p></li>
    <li class="benefit"><span class="benefit-icon"><svg viewBox="0 0 32 32"><path d="M10 9c0-4 3-6 6-6s6 2 6 6z"/><path d="M8 9h16"/><path d="M11 12h10v3H11z"/><path d="M6 19h20v10H6z"/><circle cx="11" cy="24" r="2.5"/><path d="M16 22h7M16 26h7"/></svg></span><p class="benefit-text"><strong>No Cost</strong>ID Theft Assistance</p></li>
    <li class="benefit"><span class="benefit-icon"><svg viewBox="0 0 32 32"><path d="M8 4h18v24H8z"/><path d="M12 8h10v5H12z"/><circle cx="8" cy="21" r="5"/><path d="M8 18v6M17 18h6M17 22h6M17 26h6"/></svg></span><p class="benefit-text"><strong>No Cost Tax</strong>Consultation Assistance</p></li>
    <li class="benefit"><span class="benefit-icon"><svg viewBox="0 0 32 32"><path d="M3 12c2-6 14-8 18-2"/><path d="M12 8l2 12"/><path d="M4 28l8-10h8"/><path d="M10 28l6-6M22 28l-4-6"/><circle cx="24" cy="20" r="5"/><path d="M24 17v6"/></svg></span><p class="benefit-text"><strong>Up to 17 Days of</strong>Paid Time Off</p></li>
  </ul>
</main>
</body>
</html>
```